New York College Admissions Consulting Company Looking for a One-Page Flyer Design

We are a college admissions consulting company Harwick Admissions Consulting (www.harwickadmissions.example) and we help students apply to universities. We need a 1-page flyer design to hand out at a science competition for high school students. I attach all the information that should be included in the flyer and the logo. Please make a stylistic and professional looking flyer, which will impress these very smart and sophisticated high school students and even more importantly - their parents. Feel free to move the text around the flyer and to change the font as you see fit. Also, please add a stock picture or two, as you see fit. Also, let me know if I have to pay for the stock photos (if I have to get a license to use the photos on the flyer), and where and how much I would need to pay.

Target Market(s)

Smart and sophisticated high school students and even more importantly - their parents.

Industry/Entity Type

College

Requirements
Must have
• Must look sophisticated. This is an expensive service and parents need to know that our image matches our prices.
Should not have
• Wild colors like red.

```html
<!DOCTYPE html>
<html lang="en">
<head>
<meta charset="utf-8">
<title>Complimentary Live Online Class — Harwick Admissions Consulting</title>
<link rel="stylesheet" href="https://fonts.googleapis.com/css2?family=Source+Sans+3:wght@400;600;700&family=Roboto+Condensed:wght@400;700&display=swap">
<style>
  :root {
    --page-bg: #2a2a2a;
    --paper: #ffffff;
    --sky: #3aa8e2;
    --sky-light: #63c4ef;
    --wave: #0d58a6;
    --ink-blue: #0b4f9c;
    --pill: #45b3e7;
    --tick: #6cb33e;
    --body: #5a5a5a;
    --rule: #c9c9c9;
  }
  * { box-sizing: border-box; margin: 0; padding: 0; }
  html, body { width: 1200px; height: 1124px; overflow: hidden; }
  body { background: var(--page-bg); font-family: "Source Sans 3", Arial, sans-serif; }

  .flyer {
    position: absolute; left: 214px; top: 32px;
    width: 772px; height: 1060px;
    background: var(--paper); overflow: hidden;
  }
  .flyer-header { position: absolute; left: 0; top: 0; width: 772px; height: 560px; }

  .headline { position: absolute; left: 23px; top: 28px; color: #fff; font-weight: 700; letter-spacing: -1px; line-height: 1; }
  .headline .lead { font-size: 47px; }
  .headline .live { font-size: 74px; letter-spacing: -2px; }
  .headline .sub { display: block; font-size: 42px; margin: 4px 0 0 76px; }

  .pill { display: inline-block; background: var(--pill); color: #fff; }
  .class-title { position: absolute; left: 104px; top: 405px; width: 564px; text-align: center; font-size: 20px; font-weight: 600; padding: 2px 0 3px; }

  .section-heading {
    position: absolute; left: 23px;
    font-family: "Roboto Condensed", Arial, sans-serif; font-weight: 700;
    color: var(--ink-blue); font-size: 23px;
  }
  .learn-heading { top: 462px; }
  .facts-heading { top: 716px; left: 27px; }

  .tick-list { position: absolute; left: 23px; width: 730px; list-style: none; color: var(--body); font-size: 14.5px; line-height: 23px; }
  .tick-list li { position: relative; padding-left: 17px; }
  .tick-list li::before {
    content: ""; position: absolute; left: 1px; top: 6px; width: 5px; height: 9px;
    border: solid var(--tick); border-width: 0 2.5px 2.5px 0; transform: rotate(40deg);
  }
  .learn-list { top: 497px; }
  .facts-list { top: 750px; }

  .session { position: absolute; left: 0; top: 596px; width: 772px; text-align: center; color: var(--ink-blue); }
  .session .pill { font-size: 18px; padding: 0 6px; line-height: 22px; }
  .session .date { font-size: 30px; font-weight: 700; margin-top: 2px; }
  .session .time { font-size: 18px; margin-top: 2px; }

  .brand { position: absolute; left: 0; top: 905px; width: 772px; display: flex; justify-content: center; align-items: center; gap: 12px; }
  .brand-mark { width: 34px; height: 34px; border-radius: 50%; background: var(--wave); }
  .brand-name { font-size: 25px; font-weight: 600; color: var(--wave); letter-spacing: 0.5px; }

  .contact-rule { position: absolute; left: 191px; top: 966px; width: 390px; border-top: 1px dashed var(--rule); }
  .contact { position: absolute; left: 0; top: 974px; width: 772px; text-align: center; color: var(--ink-blue); font-family: "Roboto Condensed", Arial, sans-serif; }
  .contact .web { font-size: 19px; }
  .contact .phone { font-size: 26px; margin-top: 2px; }
</style>
</head>
<body>
  <main class="flyer">
    <svg class="flyer-header" viewBox="0 0 772 560" xmlns="http://www.w3.org/2000/svg">
      <defs>
        <linearGradient id="sky" x1="0" y1="0" x2="1" y2="1">
          <stop offset="0" stop-color="var(--sky)"/>
          <stop offset="1" stop-color="var(--sky-light)"/>
        </linearGradient>
        <linearGradient id="photoTone" x1="0" y1="0" x2="0" y2="1">
          <stop offset="0" stop-color="#b9cdbf"/>
          <stop offset="0.45" stop-color="#c9d6d8"/>
          <stop offset="0.75" stop-color="#eef2f4"/>
          <stop offset="1" stop-color="#ffffff"/>
        </linearGradient>
      </defs>
      <rect class="photo-area" role="img" aria-label="Photo: smiling student in a bright classroom with classmates behind" x="0" y="100" width="772" height="460" fill="url(#photoTone)"/>
      <path class="header-wave" d="M0 400 C120 300 300 180 772 150 V88 C420 100 160 200 0 370 Z" fill="var(--wave)"/>
      <path class="header-sky" d="M0 0 H772 V118 C420 126 170 220 0 388 Z" fill="url(#sky)"/>
    </svg>

    <h1 class="headline"><span class="lead">Complimentary</span> <span class="live">Live</span><span class="sub">Online Class</span></h1>

    <p class="pill class-title">“The College Personal Statement and Perfecting Your Narrative”</p>

    <h2 class="section-heading learn-heading">Learn How To:</h2>
    <ul class="tick-list learn-list">
      <li>Avoid the Most Common Mistakes Made in The Personal Statement</li>
      <li>Compose a Memorable Essay</li>
      <li>Craft a Compelling Narrative</li>
    </ul>

    <section class="session">
      <span class="pill">Live Answers to Live Questions</span>
      <p class="date">Sunday, May 31, 2015</p>
      <p class="time">4 pm-5 pm EST</p>
    </section>

    <h2 class="section-heading facts-heading">Admission Facts and Tips:</h2>
    <ul class="tick-list facts-list">
      <li>In the last 9 years, the Average Ivy League College Admission Rate has dropped by 49%.</li>
      <li>Admission Rate in 2005 - 17.1%</li>
      <li>Admission Rate in 2014 - 8.8%</li>
      <li>The Personal Statement and the Supplemental Essays comprise approximately 25% of the admission criteria.</li>
      <li>Crafting the Perfect Narrative is vital to your college application. It can mean the difference between an acceptance and a rejection.</li>
    </ul>

    <div class="brand">
      <span class="brand-mark"></span>
      <span class="brand-name">Harwick Admissions Consulting</span>
    </div>
    <div class="contact-rule"></div>
    <footer class="contact">
      <p class="web">www.harwickadmissions.example</p>
      <p class="phone">1.646.555.0142</p>
    </footer>
  </main>
</body>
</html>
```